Investment Fee Schedule for Wealth Management Firm

We are a Chicago based firm that wants to illustrate our fee schedule for our Portfolios at different investment amounts. i.e. $50k & Under, $50k-$100k, $1-$250k, $250k-$750, $750-$1M etc. The idea is that the more money people invest they receive a volume discount. Each category has 4 portfolios with differing investment risk (Conservative, Balanced, Growth, Aggressive). Each portfolio is made up of Equities & Fixed Income shown as 20/80, 40/60/ 60/40 and 80/20. Need to name the Levels and make it easy for potential clients to understand. The attached is my sketch of how I came to price each model and might assist you in seeing how it works. May seem a bit complicated but really its just a variation on a theme. We need help communicating this in a marketing piece. We are easy to talk and work with. Hope to partner with you! Thank you for your consideration.

Update Brief 11/27/18
Some of the info I provided is not necessary and can be omitted. I would like the pie charts to be more traditional where the pie is broken down into solid color inside the circle.

Can we also take the table that you have at the top under the pie charts and expand on it? I believe that the top line should be a banner that says the companies being invested in. Under the 20/80 and 40/60 pies it would say the investment firms being used. Then the next line on this left side of the page in the same table would begin the pricing models starting with the word Level instead of tier.

Tidewell Ridge-Korvane Capital-Brimley-Hollisend
Level 1A ($3.5M+) 1.06%
Level 1B ($2.5M-$3.5M) 1.16%
Level 1C ($1.5M-$2.5M) 1.21%
Level 1D ($$750k-$1.5M) 1.26%

On the right side under the 60/40 and 80/20 pie the banner would say:

Korvane Capital-Steadfield Growth Advisors-Brimley-Hollisend
Level 1A ($3.5M+) 1.08%
Level 1B ($2.5M-$3.5M) 1.18%
Level 1C ($1.5M-$2.5M) 1.23%
Level 1D ($$750k-$1.5M) 1.28%

Below these two tables would be two more tables maybe in a different shade to distinguish it from the Level one tables.

The banner again would show the investment firms being used under the two models 20/80 and 40/60.

Level 2 ($250k-$750k) 1.39%

Tidewell Ridge-Korvane Capital-Hollisend
Level 3 ($100k-$250k) 1.45%

The next two Levels would have the banner run along the whole width of the page under all of the four models since they are using the same investment management firms.

Korvane Capital-Hollisend
Level 4($50k-$100k) 1.50%

Hollisend-Quillmont
ETF Select (Under $50k) 1.25%

Korvane Capital-Steadfield Growth Advisors-Hollisend-Brimley
Level 2 ($250k-$750k) 1.41%

Korvane Capital-Steadfield Growth Advisors-Hollisend

I really tried to convey my vision but it's a bit hard to do so in words. I would be happy to email you a hand written copy of what I just said above.

Thank you!
Derek M.

```html
<!DOCTYPE html>
<html lang="en">
<head>
<meta charset="utf-8">
<title>Tier 3 and Tier 4 Account Fee Schedule</title>
<link rel="stylesheet" href="https://fonts.googleapis.com/css2?family=Montserrat:wght@400;500;600;700;800&display=swap">
<style>
  :root {
    --backdrop: #1d4a70;
    --page: #ffffff;
    --ink: #1e2328;
    --cyan: #2bb5e8;
    --cyan-light: #7fd3f2;
    --blue: #1272bc;
    --blue-row-a: #c9e0f1;
    --blue-row-b: #afd0ea;
    --green: #4cb84a;
    --red: #a5182a;
    --red-row-a: #f1cfd5;
    --red-row-b: #e5b3bc;
    --orange: #eaa21c;
    --crimson: #b81f3c;
    --sky: #3196d6;
    --teal: #24a382;
    --grey-row-a: #dcdcdc;
    --grey-row-b: #c6c6c6;
    --text-soft: #3a3f45;
  }
  * { box-sizing: border-box; margin: 0; padding: 0; }
  html, body {
    width: 1200px; height: 675px; overflow: hidden;
    background: var(--backdrop);
    font-family: "Montserrat", sans-serif;
  }
  .flyer {
    position: absolute; left: 340px; top: 16px;
    width: 520px; height: 643px;
    background: var(--page);
    display: flex; flex-direction: column;
    overflow: hidden;
  }
  /* top bar */
  .flyer-top {
    position: relative; height: 50px;
    background: var(--ink);
    border-bottom: 4px solid var(--cyan);
  }
  .tier-ribbon {
    position: absolute; left: 16px; top: 18px;
    background: var(--cyan); color: #fff;
    font-weight: 800; font-size: 19px; letter-spacing: .5px;
    padding: 5px 34px 5px 28px;
    clip-path: polygon(0 0, 100% 0, 92% 100%, 0 100%);
  }
  .range-top {
    position: absolute; right: 18px; top: 12px;
    color: var(--cyan); font-weight: 800; font-size: 19px;
  }
  /* tier body */
  .tier-body {
    display: grid; grid-template-columns: 1fr 1fr; gap: 22px;
    padding: 10px 22px 8px;
  }
  .fee-panel { display: flex; flex-direction: column; align-items: center; }
  .intro {
    text-align: center; font-size: 9.5px; line-height: 1.25;
    color: var(--text-soft);
  }
  .intro strong { color: var(--accent); font-weight: 700; }
  .pies { display: flex; gap: 12px; margin: 6px 0 4px; }
  .pie { width: 78px; height: 78px; }
  .pie .main { fill: var(--pie-main); }
  .pie .slice { fill: var(--pie-slice); }
  .pie text { fill: #fff; font-weight: 700; font-size: 11px; text-anchor: middle; dominant-baseline: middle; font-family: "Montserrat", sans-serif; }
  .firms {
    font-size: 9px; font-weight: 700; color: var(--caption);
    text-align: center; margin-bottom: 3px;
  }
  .fee-table { width: 100%; border-collapse: collapse; font-size: 10px; color: var(--ink); }
  .fee-table th {
    background: var(--head); color: #fff; font-weight: 600;
    text-align: left; padding: 3px 6px; height: 17px;
  }
  .fee-table th.pct { text-align: center; }
  .fee-table td { padding: 3px 6px; height: 17px; border-right: 1px solid rgba(255,255,255,.7); }
  .fee-table tr:nth-child(odd) td { background: var(--row-a); }
  .fee-table tr:nth-child(even) td { background: var(--row-b); }
  .fee-table td.pct { text-align: center; border-right: 0; }
  .fee-table .total { color: var(--accent); font-weight: 600; }

  .theme-blue   { --accent: var(--blue); --pie-main: var(--blue); --pie-slice: var(--green); --caption: var(--green); --head: var(--blue); --row-a: var(--blue-row-a); --row-b: var(--blue-row-b); }
  .theme-red    { --accent: var(--red); --pie-main: var(--red); --pie-slice: var(--orange); --caption: var(--orange); --head: var(--red); --row-a: var(--red-row-a); --row-b: var(--red-row-b); }
  .theme-dark   { --accent: var(--teal); --pie-main: var(--ink); --pie-slice: var(--teal); --caption: var(--teal); --head: var(--ink); --row-a: var(--grey-row-a); --row-b: var(--grey-row-b); }
  .theme-crimson{ --accent: var(--crimson); --pie-main: var(--crimson); --pie-slice: var(--sky); --caption: var(--sky); --head: var(--crimson); --row-a: var(--red-row-a); --row-b: var(--red-row-b); }
  .theme-crimson .intro strong { color: var(--red); }
  .theme-dark .intro strong { color: var(--teal); }

  /* divider */
  .tier-divider {
    position: relative; height: 34px; margin-top: 4px;
    display: flex; align-items: center;
  }
  .tier-divider::before {
    content: ""; position: absolute; left: 0; right: 0; top: 11px;
    height: 5px; background: var(--ink);
  }
  .tier-heading {
    position: relative; margin-left: 28px; margin-top: 14px;
    background: var(--page); padding: 0 8px;
    font-weight: 800; font-size: 19px; color: var(--ink);
  }
  .range-badge {
    position: absolute; right: 150px; top: 0;
    background: var(--blue); color: #fff;
    font-weight: 800; font-size: 16px; padding: 3px 10px;
  }
  .flyer-bottom {
    margin-top: auto; height: 18px;
    background: linear-gradient(90deg, var(--cyan) 0 60%, var(--cyan-light) 60%);
    border-top: 3px solid #fff;
  }
</style>
</head>
<body>
<main class="flyer">
  <header class="flyer-top">
    <div class="tier-ribbon">TIER - 3 ACCOUNT</div>
    <div class="range-top">$250K-$750K</div>
  </header>

  <section class="tier-body">
    <div class="fee-panel theme-blue">
      <p class="intro">The companies being invested in.<br><strong>Under the 20/80 and 40/60 pies it would say</strong><br>the investment firms being used.</p>
      <div class="pies">
        <svg class="pie" viewBox="0 0 100 100"><circle class="main" cx="50" cy="50" r="44"/><path class="slice" d="M50 50 L50 6 A44 44 0 0 1 91.85 36.4 Z"/><text x="64" y="30">20%</text><text x="36" y="70">80%</text></svg>
        <svg class="pie" viewBox="0 0 100 100"><circle class="main" cx="50" cy="50" r="44"/><path class="slice" d="M50 50 L50 6 A44 44 0 0 1 75.86 85.6 Z"/><text x="73" y="42">40%</text><text x="28" y="58">60%</text></svg>
      </div>
      <p class="firms">Tidewell Ridge-Korvane Capital-Brimley-Hollisend</p>
      <table class="fee-table">
        <tr><th>Particular</th><th></th><th class="pct">%</th></tr>
        <tr><td>Tidewell Ridge</td><td>Platform</td><td class="pct">0.30%</td></tr>
        <tr><td>Korvane Capital</td><td>Mar..</td><td class="pct">0.24%</td></tr>
        <tr><td>Brimley</td><td>Rep..</td><td class="pct">0.85%</td></tr>
        <tr><td class="total">Hollisend</td><td></td><td class="pct total">1.39%</td></tr>
      </table>
    </div>

    <div class="fee-panel theme-red">
      <p class="intro">The companies being invested in.<br><strong>under the 60/40 and 80/20 pies it would say</strong><br>the investment firms being used.</p>
      <div class="pies">
        <svg class="pie" viewBox="0 0 100 100"><circle class="main" cx="50" cy="50" r="44"/><path class="slice" d="M50 50 L50 6 A44 44 0 0 1 75.86 85.6 Z"/><text x="73" y="42">40%</text><text x="28" y="58">60%</text></svg>
        <svg class="pie" viewBox="0 0 100 100"><circle class="main" cx="50" cy="50" r="44"/><path class="slice" d="M50 50 L50 6 A44 44 0 0 1 91.85 36.4 Z"/><text x="64" y="30">20%</text><text x="36" y="70">80%</text></svg>
      </div>
      <p class="firms">Korvane Capital-Steadfield Growth Advisors-Hollisend-Brimley</p>
      <table class="fee-table">
        <tr><th>Particular</th><th></th><th class="pct">%</th></tr>
        <tr><td>Tidewell Ridge</td><td>Platform</td><td class="pct">0.30%</td></tr>
        <tr><td>Korvane Capital</td><td>Mar..</td><td class="pct">0.26%</td></tr>
        <tr><td>Brimley</td><td>Rep..</td><td class="pct">0.85%</td></tr>
        <tr><td class="total">Hollisend</td><td></td><td class="pct total">1.41%</td></tr>
      </table>
    </div>
  </section>

  <div class="tier-divider">
    <h2 class="tier-heading">TIER - 4 ACCOUNT</h2>
    <div class="range-badge">$100K-$250K</div>
  </div>

  <section class="tier-body">
    <div class="fee-panel theme-dark">
      <p class="intro">The companies being invested in.<br><strong>Under the 20/80 and 40/60 pies it would say</strong><br>the investment firms being used.</p>
      <div class="pies">
        <svg class="pie" viewBox="0 0 100 100"><circle class="main" cx="50" cy="50" r="44"/><path class="slice" d="M50 50 L50 6 A44 44 0 0 1 91.85 36.4 Z"/><text x="64" y="30">20%</text><text x="36" y="70">80%</text></svg>
        <svg class="pie" viewBox="0 0 100 100"><circle class="main" cx="50" cy="50" r="44"/><path class="slice" d="M50 50 L50 6 A44 44 0 0 1 75.86 85.6 Z"/><text x="73" y="42">40%</text><text x="28" y="58">60%</text></svg>
      </div>
      <p class="firms">Tidewell Ridge-Korvane Capital-Brimley-Hollisend</p>
      <table class="fee-table">
        <tr><th>Particular</th><th></th><th class="pct">%</th></tr>
        <tr><td>Tidewell Ridge</td><td>Platform</td><td class="pct">0.30%</td></tr>
        <tr><td>Korvane Capital</td><td>Mar..</td><td class="pct">0.24%</td></tr>
        <tr><td>Brimley</td><td>Rep..</td><td class="pct">0.85%</td></tr>
        <tr><td class="total">Hollisend</td><td></td><td class="pct total">1.39%</td></tr>
      </table>
    </div>

    <div class="fee-panel theme-crimson">
      <p class="intro">The companies being invested in.<br><strong>under the 60/40 and 80/20 pies it would say</strong><br>the investment firms being used.</p>
      <div class="pies">
        <svg class="pie" viewBox="0 0 100 100"><circle class="main" cx="50" cy="50" r="44"/><path class="slice" d="M50 50 L50 6 A44 44 0 0 1 75.86 85.6 Z"/><text x="73" y="42">40%</text><text x="28" y="58">60%</text></svg>
        <svg class="pie" viewBox="0 0 100 100"><circle class="main" cx="50" cy="50" r="44"/><path class="slice" d="M50 50 L50 6 A44 44 0 0 1 91.85 36.4 Z"/><text x="64" y="30">20%</text><text x="36" y="70">80%</text></svg>
      </div>
      <p class="firms">Korvane Capital-Steadfield Growth Advisors-Hollisend-Brimley</p>
      <table class="fee-table">
        <tr><th>Particular</th><th></th><th class="pct">%</th></tr>
        <tr><td>Tidewell Ridge</td><td>Platform</td><td class="pct">0.30%</td></tr>
        <tr><td>Korvane Capital</td><td>Mar..</td><td class="pct">0.26%</td></tr>
        <tr><td>Brimley</td><td>Rep..</td><td class="pct">0.85%</td></tr>
        <tr><td class="total">Hollisend</td><td></td><td class="pct total">1.41%</td></tr>
      </table>
    </div>
  </section>

  <footer class="flyer-bottom"></footer>
</main>
</body>
</html>
```